Etiketten für Gin
Zielgruppe
Wir sind eine kleine neue Brennerei im bayerischen Oberland und werden unter den Namen „Morgentau“ und „Morgentau Zitrone“ zwei GIN-Sorten auf den Markt bringen.
Der GIN wird online und vor Ort verkauft und sollte daher eine exklusiv-auffällige Optik haben um die Kunden zu beeindrucken. Zielkunden sind anspruchsvolle Genießer, welche die bayerische Gastlichkeit und Lebenskultur schätzen.
Neu an den beiden Gins ist, dass sie mit Blütenpollen destilliert werden, was auf dem Etikett erscheinen muss.
Aufgabenstellung
Wir suchen zwei sich ähnelnde GIN-Etiketten deren Design ausdrückt, dass es sich um handgemachte und hochwertige GIN handelt, deren Zutat Blütenpollen bisher einzigartig ist.
Statt der oft üblichen Bezeichnung „London Dry Gin“ soll „Hochbrand Dry Gin“ und „handcrafted“ auf dem Etikett erscheinen, zusätzlich natürlich die verkehrsüblichen Angaben.
Abgefüllt wird in weißen 500ml Flaschen Typ Ventra mit Korkverschluss von flaschenhof-beispiel.com.
Sinnvoll halten wir ein Frontetikett, lassen aber gerne auch andere Vorschläge zu.

```html
<!DOCTYPE html>
<html lang="de">
<head>
<meta charset="utf-8">
<title>Morgentau – Hochbrand Dry Gin Etikett</title>
<link rel="stylesheet" href="https://fonts.googleapis.com/css2?family=Arvo:wght@400;700&family=Josefin+Sans:wght@400&family=Open+Sans:wght@400;700;800&display=swap">
<style>
  :root {
    --band-green: #80da5c;
    --title-green: #7dd85a;
    --artwork-tone-a: #d9ebe5;
    --artwork-tone-b: #c3ddd4;
    --ink: #404040;
    --paper: #ffffff;
  }
  * { margin: 0; padding: 0; box-sizing: border-box; }
  html, body { width: 1200px; height: 801px; overflow: hidden; background: var(--paper); }
  .label {
    position: relative;
    width: 1200px;
    height: 801px;
    background: var(--paper);
    color: var(--ink);
    font-family: "Open Sans", sans-serif;
  }
  .band { position: absolute; left: 0; width: 100%; background: var(--band-green); }
  .band--top { top: 0; height: 59px; }
  .band--bottom { bottom: 0; height: 59px; }

  .artwork-area {
    position: absolute;
    left: 521px;
    top: 102px;
    width: 158px;
    height: 166px;
    border-radius: 12px;
    background: linear-gradient(160deg, var(--artwork-tone-a), var(--artwork-tone-b));
  }

  .product-name {
    position: absolute;
    left: 0;
    width: 100%;
    top: 338px;
    text-align: center;
    font-family: "Arvo", serif;
    font-weight: 400;
    font-size: 100px;
    line-height: 1;
    color: var(--title-green);
    -webkit-text-stroke: 1.5px var(--title-green);
  }

  .product-type {
    position: absolute;
    left: 0;
    width: 100%;
    top: 564px;
    text-align: center;
    font-family: "Josefin Sans", sans-serif;
    font-size: 25px;
    letter-spacing: 4px;
    line-height: 31px;
    text-transform: uppercase;
    color: var(--ink);
  }

  .volume {
    position: absolute;
    left: 0;
    width: 100%;
    top: 706px;
    text-align: center;
    font-weight: 800;
    font-size: 19px;
    letter-spacing: 2.5px;
    color: var(--ink);
  }

  .story, .legal-note {
    position: absolute;
    left: 45px;
    width: 215px;
    font-size: 12px;
    line-height: 23px;
    letter-spacing: 1.4px;
    color: var(--ink);
  }
  .story { top: 323px; }
  .legal-note { top: 620px; }

  .distributor {
    position: absolute;
    left: 929px;
    width: 200px;
    top: 309px;
    text-align: center;
    font-size: 11.5px;
    line-height: 13.5px;
    letter-spacing: 0.9px;
    color: var(--ink);
  }

  .recycle-note {
    position: absolute;
    right: 56px;
    top: 453px;
    text-align: right;
    font-weight: 700;
    font-size: 10px;
    line-height: 18px;
    letter-spacing: 1px;
    color: var(--ink);
  }
</style>
</head>
<body>
  <main class="label">
    <div class="band band--top"></div>

    <div class="artwork-area" role="img" aria-label="Platz für die Bildmarke der Brennerei"></div>

    <h1 class="product-name">Morgentau</h1>

    <p class="product-type">Hochbrand Dry Gin<br>–<br>Handcrafted</p>

    <p class="volume">500 ML</p>

    <p class="story">Wir sind eine kleine neue Brauerei im bayerischen Oberland. Das neue an unserem Gin ist, dass sie mit Blütenpollen destilliert wird. Unser hochwertiger Gin wird in Handarbeit gefertigt.Zur destilierung nutzen wir Blütenpollen was bisher einzigartig ist.</p>

    <p class="legal-note">Hier könnten Inhaltsangaben und Alkoholgehalt stehen</p>

    <p class="distributor">Vertrieben durch:<br>Name der Brennerei<br>mit Anschrift</p>

    <p class="recycle-note">Bitte recyceln Sie diese Flasche<br>nach der Verwendung.</p>

    <div class="band band--bottom"></div>
  </main>
</body>
</html>
```